Boat Hire Website - Building on the existing web design

Keel Charter Harbour connects boat owners with people looking to charter a boat for their next big event.
There are now over 30 boats to choose from, so I need a nifty filter system to instantly reduce 30 boats down to a small number, based on some user preferences.
I want to use Ajax or similar so that the collection of boats instantly changes in front of you, rather than reloading.

Here is the page we are working with:
http://www.keelcharterharbour.com.au/c/all_boats

The page should not look drastically different to every other page on the site, so I suggest keeping the entire header section and the blue background but I'm open to ideas.
Your goal is to add dials / gauges / filters / input boxes or whetever way you can think of to allow the user to filter the list of suitable boats for them.
The attributes they can adjust are:
1. Number of guests (overall max is 400)
2. Budget (not exact figures, more like Luxury, Mid-High Range, Mid Range, Budget).

I suggest changing the profile images to make them very small so you can see them all on one page.
It's optional whether you keep all the other info on each boat, such as the short description, the attributes such as BBQ, the enquiry forms.
You must keep the Boat hire cost and the suitable for x number of guests part in some way for each boat.

Things we like:
Smooth, cool designs
Very easy to understand and use

Things we don't want:
Pagination
Updates

Hey All,

Just to let you know, I've now guaranteed payment.

Thanks to the 2 designers for their work so far.

Reg.

Thanks for all the designs to date, we're getting closer but still not quite there yet.

Here's a summary of what's been working well so far:
1. Leave the header of the page untouched (http://www.keelcharterharbour.com.au/c/all_boats) from the logo down to the water line.
2. I like 2 horizontal sliders below the water line for filtering on number of guests and Quality/Budget. Ideally not taking too much vertical space.
3. I like small tiled boat images representing each boat, with at least 3 in each row. 
I like designs where hovering over the individual boat images blacks it out and reveals more info such as price, number of guests, short description, Enquire and (More Info) buttons. Unfortunately I don't think there's enough space to show the attributes such as BBQ?
The more boat images I can see above the fold the better, but unfortunately the smaller they are, the less room there is for extra info to be displayed when hovering over them.

Thanks and I look forward to more designs in the next couple of days.

Target Market(s)

Age 21 - 50

Industry/Entity Type

Building

```html
<!DOCTYPE html>
<html lang="en">
<head>
<meta charset="utf-8">
<title>Keel Charter Harbour – All Boats</title>
<link rel="stylesheet" href="https://fonts.googleapis.com/css2?family=Arimo:ital,wght@0,400;0,700;1,700&family=Michroma&display=swap">
<style>
:root{
  --sky-top:#3d93d4;
  --sky-mid:#8fcdf0;
  --sky-glow:#e6f6fd;
  --sea-top:#58bde8;
  --sea-deep:#1b8fcd;
  --ink:#163c63;
  --ink-soft:#2b5a85;
  --white:#ffffff;
  --nav-top:#47aedd;
  --nav-bot:#1b7dbf;
  --panel:rgba(255,255,255,0.28);
  --rule:rgba(22,60,99,0.35);
  --orange:#ff7f12;
  --btn:#1f7db7;
  --btn-edge:#0f3453;
  --photo-city:#8aa9c4;
  --photo-water:#4f86b0;
}
*{box-sizing:border-box;margin:0;padding:0}
html,body{width:1200px;height:936px;overflow:hidden}
body{font-family:"Arimo",Arial,sans-serif;color:var(--ink)}
.canvas{position:relative;width:1200px;height:936px;overflow:hidden;
  background:
    radial-gradient(ellipse 260px 170px at 560px 40px,rgba(255,255,255,.75),transparent 70%),
    radial-gradient(ellipse 700px 340px at 600px 470px,rgba(200,240,255,.55),transparent 70%),
    linear-gradient(180deg,var(--sky-top) 0,var(--sky-mid) 200px,var(--sky-glow) 360px,var(--sea-top) 378px,#7fd0f0 470px,var(--sea-top) 620px,var(--sea-deep) 936px);}
.abs{position:absolute}
.brand{left:188px;top:82px;width:230px;font-size:27px;font-weight:700;color:#1c4d86;line-height:1.1;display:flex;align-items:center;gap:10px}
.brand .mark{width:16px;height:16px;border-radius:50%;background:#ff8a1c;flex:none}
.helpline{left:506px;top:63px;font-size:24px;color:var(--ink)}
.field-label{font-size:15px;letter-spacing:.5px;color:var(--ink)}
.question-label{left:506px;top:101px}
.quote-label{left:789px;top:101px}
.question-box{left:505px;top:124px;width:262px;height:29px;background:#fff;border:1px solid #9bb3c8;font-size:13px;color:#8a8a8a;padding:4px 3px}
.email-box{left:788px;top:125px;width:258px;height:26px;background:#fff;border:1px solid #9bb3c8;font-size:14px;color:#8a8a8a;padding:5px 2px}
.main-nav{left:148px;top:197px;width:898px;height:47px;border-radius:4px;background:linear-gradient(180deg,var(--nav-top),var(--nav-bot))}
.main-nav a{position:absolute;top:14px;font-size:14.5px;color:#eaf6ff;text-decoration:none}
.main-nav a.current{color:#fff;font-weight:700;letter-spacing:-.3px}
.main-nav .divider{position:absolute;left:608px;top:8px;width:1px;height:31px;background:rgba(255,255,255,.45)}
.finder{left:148px;top:253px;width:898px;height:196px;background:var(--panel);border-radius:3px}
.display{font-family:"Michroma",sans-serif;color:var(--ink);letter-spacing:1px}
.finder-title{left:197px;top:271px;font-size:19px}
.finder-sub{font-size:16px}
.select{left:194px;top:327px;width:224px;height:27px;border:2px solid #fff;background:linear-gradient(180deg,#3fb2ec,#1e96dc);font-size:11.5px;font-weight:700;color:var(--ink);padding:5px 9px}
.select svg{position:absolute;right:6px;top:6px}
.track{height:5px;border:1px solid #6d8aa6;background:#fff;border-radius:2px}
.tick-marks{position:absolute;left:0;right:0;top:4px;height:6px;background:repeating-linear-gradient(90deg,#6d8aa6 0 1px,transparent 1px 22.5px)}
.thumb{position:absolute;top:-5px;width:10px;height:16px;background:linear-gradient(#2e7fcf,#0f4f99);border-radius:2px 2px 5px 5px}
.small{font-size:12px;color:var(--ink)}
.services{left:194px;top:384px;width:623px;height:37px;border:2px solid rgba(255,255,255,.85);background:rgba(255,255,255,.18);display:flex;align-items:center;gap:18px;padding-left:16px;font-size:12px;font-weight:700}
.services span{display:flex;align-items:center;gap:10px}
.services i{width:11px;height:11px;background:#fff;border:1px solid #8a9bab;display:inline-block}
.find-now{left:829px;top:383px;width:168px;height:39px;background:var(--orange);color:var(--ink);font-weight:700;font-style:italic;font-size:23px;text-align:center;line-height:39px;letter-spacing:-.5px}
.waterline{left:0;top:395px}
.section-rule{left:148px;top:456px;width:898px;height:1px;background:var(--ink-soft)}
.page-title{left:148px;top:458px;font-size:24px;color:var(--ink)}
.count{left:148px;top:493px;font-size:17px;color:var(--ink-soft)}
.boat-name{font-size:23px;color:#fff;left:148px}
.photo{left:148px;width:412px;border-radius:3px;background:linear-gradient(180deg,#cfe2ef 0,var(--photo-city) 45%,var(--photo-water) 80%,#3f79a6 100%)}
.specs{left:578px;width:486px;font-size:13px;color:var(--ink)}
.specs .row{position:relative;height:28px;border-bottom:1px solid var(--rule)}
.specs .row:last-child{border-bottom:0}
.specs .row span{position:absolute;top:6px}
.specs .row svg{position:absolute;top:9px}
.desc{left:578px;top:688px;width:420px;font-size:13.5px;line-height:19px;color:var(--ink-soft)}
.btn{height:41px;width:167px;border:1px solid var(--btn-edge);border-radius:3px;background:var(--btn);color:#fff;font-size:11.5px;font-weight:700;display:flex;align-items:center;justify-content:center;text-align:center;line-height:14px}
.list-rule{left:148px;top:868px;width:916px;height:1px;background:rgba(255,255,255,.3)}
</style>
</head>
<body>
<div class="canvas">

  <div class="abs brand"><span class="mark"></span>Keel Charter Harbour</div>

  <div class="abs helpline">Get help from Keel Charter Harbour - 0400 555 018</div>
  <div class="abs field-label question-label">Ask a general question:</div>
  <div class="abs field-label quote-label">Get multiple quotes fast:</div>
  <div class="abs question-box">How can we help?</div>
  <div class="abs email-box">Enter your email address</div>

  <nav class="abs main-nav">
    <a style="left:70px">Home</a>
    <a style="left:156px">Parties</a>
    <a style="left:248px">Weddings</a>
    <a style="left:359px">Corporate events</a>
    <a class="current" style="left:517px">All Boats</a>
    <span class="divider"></span>
    <a style="left:644px">Useful info</a>
    <a style="left:758px">My Charter</a>
  </nav>

  <div class="abs finder"></div>
  <svg class="abs waterline" width="1200" height="80" viewBox="0 0 1200 80">
    <path d="M0 40 C250 30 450 60 700 48 S1050 20 1200 30" fill="none" stroke="rgba(255,255,255,.7)" stroke-width="3"/>
    <path d="M0 48 C250 40 450 70 700 58 S1050 30 1200 40" fill="none" stroke="rgba(30,120,190,.35)" stroke-width="5"/>
  </svg>

  <div class="abs display finder-title">FIND A BOAT</div>
  <div class="abs display finder-sub" style="left:197px;top:302px">BOATS</div>
  <div class="abs select">ALL BOATS
    <svg width="20" height="12" viewBox="0 0 20 12"><path d="M2 2 L10 10 L18 2" fill="none" stroke="#163c63" stroke-width="2.5"/></svg>
  </div>
  <div class="abs display finder-sub" style="left:197px;top:360px">OTHER SERVICES</div>

  <div class="abs display finder-sub" style="left:475px;top:302px">GUESTS</div>
  <div class="abs small" style="left:636px;top:303px">1-49 Guests</div>
  <div class="abs track" style="left:477px;top:330px;width:225px"><div class="tick-marks"></div><div class="thumb" style="left:2px"></div></div>
  <div class="abs small" style="left:478px;top:346px;font-weight:700">0</div>
  <div class="abs small" style="left:658px;top:346px;font-weight:700">400max</div>

  <div class="abs display finder-sub" style="left:756px;top:302px">BUDGET</div>
  <div class="abs track" style="left:758px;top:330px;width:225px"><div class="tick-marks" style="background:repeating-linear-gradient(90deg,#6d8aa6 0 1px,transparent 1px 56px)"></div><div class="thumb" style="left:0"></div></div>
  <div class="abs small" style="left:750px;top:346px">Luxury</div>
  <div class="abs small" style="left:797px;top:346px">Mid-High Range</div>
  <div class="abs small" style="left:888px;top:346px">Mid Range</div>
  <div class="abs small" style="left:955px;top:346px">Budget</div>

  <div class="abs services">
    <span><i></i>Catering</span>
    <span><i></i>Licensed bar</span>
    <span><i></i>BBQ</span>
    <span><i></i>DJ/dance floor</span>
    <span><i></i>BYO food option</span>
    <span><i></i>BYO drinks option:</span>
  </div>
  <div class="abs find-now">FIND NOW!</div>

  <div class="abs section-rule"></div>
  <h1 class="abs page-title" style="font-weight:400">All Boats</h1>
  <div class="abs count">Displaying 1 - 10 of 22 Boats for hire</div>

  <h2 class="abs boat-name" style="top:521px;font-weight:400">Wattlebay</h2>
  <div class="abs photo" style="top:563px;height:284px" role="img" aria-label="Photo of a white motor cruiser on the harbour with city towers behind"></div>
  <div class="abs specs" style="top:557px">
    <div class="row"><span style="left:0">Suits:</span><span style="left:118px">1-49 Guests</span><span style="left:211px">Boat hire only cost:</span><span style="right:0">$3,400 - $4,400 / 4 hours</span></div>
    <div class="row"><span style="left:0">Catering:</span>
      <svg style="left:122px" width="10" height="10" viewBox="0 0 10 10"><path d="M1 5 L4 8 L9 1" fill="none" stroke="#fff" stroke-width="2"/></svg>
      <span style="left:213px">Licensed bar:</span>
      <svg style="left:402px" width="10" height="10" viewBox="0 0 10 10"><path d="M1 5 L4 8 L9 1" fill="none" stroke="#fff" stroke-width="2"/></svg></div>
    <div class="row"><span style="left:0">BBQ:</span>
      <svg style="left:122px" width="10" height="10" viewBox="0 0 10 10"><path d="M2 2 L8 8 M8 2 L2 8" stroke="#fff" stroke-width="2"/></svg>
      <span style="left:213px">DJ/dance floor:</span>
      <svg style="left:402px" width="10" height="10" viewBox="0 0 10 10"><path d="M2 2 L8 8 M8 2 L2 8" stroke="#fff" stroke-width="2"/></svg></div>
    <div class="row"><span style="left:0">BYO food option:</span>
      <svg style="left:122px" width="10" height="10" viewBox="0 0 10 10"><path d="M1 5 L4 8 L9 1" fill="none" stroke="#fff" stroke-width="2"/></svg>
      <span style="left:213px">BYO drinks option:</span>
      <svg style="left:402px" width="10" height="10" viewBox="0 0 10 10"><path d="M1 5 L4 8 L9 1" fill="none" stroke="#fff" stroke-width="2"/></svg></div>
  </div>
  <p class="abs desc">This is the perfect vessel for corporate entertaining, built to offer superlative luxury for the discerning guest.</p>
  <div class="abs btn" style="left:578px;top:757px">Get a Quote /<br>Make an Enquiry</div>
  <div class="abs btn" style="left:792px;top:757px">More Info</div>

  <div class="abs list-rule"></div>
  <h2 class="abs boat-name" style="top:870px;font-weight:400">Pontoon</h2>
  <div class="abs photo" style="top:911px;height:40px;background:linear-gradient(180deg,#e9eef1,#c9d4db)" role="img" aria-label="Photo of a large pontoon vessel's covered deck"></div>
  <div class="abs specs" style="top:904px">
    <div class="row"><span style="left:0">Suits:</span><span style="left:102px">60-300 Guests</span><span style="left:211px">Boat hire only cost:</span><span style="right:0">$3,600 - $4,000 / 4 hours</span></div>
  </div>

</div>
</body>
</html>
```